Corvel Ridge New Website Design

We just changed our logo (thank you PlanHarbor) and company name change from Corvel Ridge Machining to Corvel Ridge Manufacturing. We do CNC Swiss screw machining and multi-axis machines. We make parts for many industries. We make large quantity production parts as well small R&D quantities. You can look at our current (outdated) website: http://www.corvelridgemachining.example to see what we do. We would like a WordPress site, including contact form for "request for quote" . We would also like it to be mobile friendly, and the ability to maintain it ourselves after it is finished I have included our new logo and fonts for references. We would like our site to convey the feeling of precision, capability, and trust worthiness with a very modern look. The new website address is www.corvelridge-mfg.example

Coding

Coded - Design and coding required

Number of Pages Required

5+ page

Font styles to use
Serif
Sans Serif
Other font styles liked:
• fronts included, not sure if they work

Colors

Designer to choose colors to be used in the design.

Requirements
Must have
• Contact Info, request for quote field

```html
<!DOCTYPE html>
<html lang="en">
<head>
<meta charset="utf-8">
<title>Corvel Ridge Manufacturing</title>
<link rel="stylesheet" href="https://fonts.googleapis.com/css2?family=Poppins:ital,wght@0,300;0,400;0,500;0,600;0,700;1,400&family=Lora:ital@1&display=swap">
<style>
:root{
  --navy:#1d3f8c;
  --navy-deep:#183577;
  --heading:#2a3f99;
  --ink:#2c2f36;
  --muted:#6b6f78;
  --light:#f3f4f7;
  --dark:#25282e;
  --footer:#363b45;
  --footer-bar:#2b2f37;
  --white:#ffffff;
}
*{box-sizing:border-box;margin:0;padding:0}
html,body{width:1200px;height:4206px;overflow:hidden}
body{position:relative;background:var(--white);font-family:'Poppins',sans-serif;color:var(--ink)}
.abs{position:absolute}
.btn{position:absolute;display:flex;align-items:center;justify-content:center;border-radius:20px;font-size:11px;font-weight:600;letter-spacing:.5px;text-transform:uppercase}
.btn-solid{background:var(--navy);color:var(--white)}
.btn-outline{border:1.5px solid var(--navy);color:var(--navy)}
.wordmark{font-weight:700;letter-spacing:1px;text-transform:uppercase;color:var(--navy-deep);display:flex;align-items:center;gap:10px}
.wordmark .dot{width:14px;height:14px;border-radius:50%;background:var(--navy)}
.section-title{position:absolute;left:0;width:1200px;text-align:center;font-size:25px;font-weight:600;color:var(--heading)}
.section-title::after{content:"";display:block;width:130px;height:2px;background:var(--heading);margin:10px auto 0;opacity:.6}

/* header */
.site-header{position:absolute;top:0;left:0;width:1200px;height:118px;background:var(--white);z-index:3}
.site-header .wordmark{position:absolute;left:78px;top:38px;font-size:26px}
.header-call{position:absolute;left:777px;top:30px;font-size:15px;font-weight:600;color:var(--navy-deep)}
.header-quote{left:976px;top:20px;width:143px;height:39px}
.main-nav{position:absolute;top:82px;left:560px;display:flex;gap:0}
.main-nav a{font-size:13px;font-weight:500;color:var(--ink);text-decoration:none;position:absolute;white-space:nowrap}
.main-nav a.active{color:var(--navy)}

/* hero */
.hero{position:absolute;top:118px;left:0;width:1200px;height:500px;background:linear-gradient(120deg,#1b2330 0%,#4b5565 35%,#8b7a4e 50%,#3b4452 70%,#161c26 100%)}
.hero h1{position:absolute;top:160px;left:0;width:1200px;text-align:center;color:var(--white);font-size:34px;font-weight:600;letter-spacing:1.5px;line-height:38px}
.hero-cta{left:528px;top:273px;width:144px;height:36px}
.hero-dots{position:absolute;top:370px;left:544px;display:flex;gap:12px}
.hero-dots span{width:10px;height:10px;border-radius:50%;border:1.5px solid rgba(255,255,255,.8)}
.hero-dots span:first-child{background:var(--white)}
.hero-wave{position:absolute;left:0;top:480px}

/* welcome */
.welcome-label{top:694px;left:0;width:1200px;text-align:center;font-size:14px;color:var(--muted)}
.welcome .wordmark{position:absolute;top:745px;left:0;width:1200px;justify-content:center;font-size:30px}

/* about */
.about{position:absolute;top:813px;left:0;width:1200px;height:480px;background:linear-gradient(180deg,var(--white),var(--light))}
.about h2{position:absolute;left:199px;top:76px;width:340px;font-size:19px;font-weight:600;line-height:30px;color:var(--heading)}
.about p{position:absolute;left:199px;width:380px;font-size:11.5px;line-height:20px;color:var(--muted)}
.about-btn{left:199px;top:373px;width:129px;height:37px}
.about-photo{position:absolute;left:639px;top:25px;width:359px;height:441px;background:linear-gradient(160deg,#7e8ea6,#3c5a86 45%,#c9d3de 75%,#5d6f86)}

/* equipment & services */
.services-bg{position:absolute;left:0;top:1360px}
.diamond-label{position:absolute;color:var(--white);font-size:19px;font-weight:600;text-align:center;width:300px}
.circle-arrow{position:absolute;width:36px;height:36px;border-radius:50%;border:1.5px solid var(--white);display:flex;align-items:center;justify-content:center}
.more-btn{left:557px;top:1644px;width:80px;height:32px;font-size:10px}
.services-title{top:1830px;color:var(--white)}
.services-title::after{display:none}
.services-text{position:absolute;top:1886px;left:250px;width:700px;text-align:center;font-size:11.5px;line-height:19px;color:#e4e6ea}
.explore-btn{left:535px;top:2021px;width:142px;height:36px}

/* industries */
.industries{position:absolute;top:2215px;left:0;width:1200px;height:500px;background:linear-gradient(180deg,var(--white),var(--light))}
.industry{position:absolute;top:258px;width:140px;text-align:center;font-size:14px;color:var(--ink)}
.industry svg{display:block;margin:0 auto 12px}
.carousel-arrow{position:absolute;top:280px}

/* testimonials */
.testimonials{position:absolute;top:2706px;left:0;width:1200px}
.testimonials .section-title{top:70px;color:var(--white)}
.testimonials .section-title::after{background:var(--white)}
.quote{position:absolute;top:140px;left:220px;width:760px;text-align:center;font-family:'Lora',serif;font-style:italic;font-size:20px;line-height:30px;color:var(--white)}
.avatar{position:absolute;left:567px;top:226px;width:66px;height:66px;border-radius:50%;border:3px solid var(--white);background:linear-gradient(160deg,#c9b6a2,#6a5444)}
.person{position:absolute;top:300px;left:0;width:1200px;text-align:center;color:var(--white);font-size:13px;font-weight:600}
.person span{display:block;font-size:11px;font-weight:400;opacity:.85}

/* quote form */
.quote-form .section-title{top:3303px}
.field{position:absolute;height:40px;border:1px solid #dcdfe5;border-radius:4px;background:var(--white);padding:0 18px;display:flex;align-items:center;font-size:11.5px;color:#9da2ab}
.field.area{align-items:flex-start;padding-top:12px}
.submit-btn{left:544px;top:3659px;width:112px;height:37px}

/* footer */
.footer-bg{position:absolute;left:0;top:3740px}
.site-footer .wordmark{position:absolute;left:202px;top:3825px;font-size:30px;color:#9aa1ad}
.site-footer .wordmark .dot{background:#9aa1ad}
.footer-col{position:absolute;top:3934px;color:#d7dae0;font-size:12px;line-height:24px}
.footer-col h4{font-size:14px;font-weight:600;color:var(--white);margin-bottom:6px}
.footer-col .big{font-size:17px;color:var(--white)}
.footer-col .active{text-decoration:underline}
.social{position:absolute;left:966px;width:30px;height:30px;border-radius:50%;border:1px solid #8b919b}
.footer-bar{position:absolute;top:4144px;left:0;width:1200px;height:62px;background:var(--footer-bar);color:#aeb3bc;font-size:11px;display:flex;align-items:center;padding-left:199px}
</style>
</head>
<body>

<header class="site-header">
  <div class="wordmark"><span class="dot"></span>Corvel Ridge</div>
  <div class="header-call">Call Us: 555-214-7730</div>
  <a class="btn btn-solid header-quote">Get Free Quotes</a>
  <nav class="main-nav">
    <a class="active" style="left:0">Home</a>
    <a style="left:84px">About Us</a>
    <a style="left:188px">Services</a>
    <a style="left:288px">Equipment</a>
    <a style="left:401px">Quality</a>
    <a style="left:490px">Contact Us</a>
  </nav>
</header>

<section class="hero">
  <div role="img" aria-label="Close-up photograph of a CNC lathe machining a brass part" style="position:absolute;inset:0"></div>
  <h1>From Blueprint to Reality Better<br>Than you Expected</h1>
  <a class="btn btn-solid hero-cta">Contact Us</a>
  <div class="hero-dots"><span></span><span></span><span></span><span></span><span></span></div>
  <svg class="hero-wave" width="1200" height="140" viewBox="0 0 1200 140"><path d="M0 75 C220 20 420 150 660 110 C880 72 1040 20 1200 35 L1200 140 L0 140Z" fill="#ffffff"/></svg>
</section>

<section class="welcome">
  <div class="abs welcome-label">Welcome to</div>
  <div class="wordmark"><span class="dot"></span>Corvel Ridge</div>
</section>

<section class="about">
  <h2>Founded in 1996, Corvel Ridge Manufacturing Inc.</h2>
  <p style="top:150px">Corvel Ridge Machining Company is a high quality machining resource providing friendly service, fast turnaround times, and engineering expertise, at competitive pricing. With almost 28 years of experience in the industry, Corvel Ridge utilizes certified state of the art equipment partnered with top professionals to maximize the value and quality in your product.</p>
  <p style="top:270px">Specializing in precision, Corvel Ridge will provide you with superior products, at affordable prices.</p>
  <a class="btn btn-outline about-btn">About Us</a>
  <div class="about-photo" role="img" aria-label="Photograph of a milling spindle cutting metal with coolant spray"></div>
</section>

<section class="services">
  <svg class="services-bg" width="1200" height="883" viewBox="0 0 1200 883">
    <defs>
      <linearGradient id="darkFill" x1="0" y1="0" x2="1" y2="1">
        <stop offset="0" stop-color="#3a3d44"/><stop offset=".5" stop-color="#1d1f24"/><stop offset="1" stop-color="#2e3137"/>
      </linearGradient>
    </defs>
    <path role="img" aria-label="Dark photograph of machined metal parts" d="M0 190 C300 140 500 220 760 175 C960 140 1100 150 1200 165 L1200 800 C1000 840 820 760 600 820 C380 880 180 800 0 830Z" fill="url(#darkFill)"/>
    <polygon role="img" aria-label="Machining equipment photograph" points="280,0 490,196 280,393 70,196" fill="#2f57a8" opacity=".85"/>
    <polygon role="img" aria-label="Support equipment photograph" points="917,0 1127,196 917,393 707,196" fill="#2f57a8" opacity=".85"/>
    <polygon role="img" aria-label="QA equipment photograph" points="597,0 807,196 597,393 387,196" fill="#7c838d" opacity=".92"/>
  </svg>
  <div class="diamond-label" style="left:130px;top:1543px">Machining Equipment</div>
  <div class="diamond-label" style="left:447px;top:1543px">Qa Equipment</div>
  <div class="diamond-label" style="left:767px;top:1541px">Support Equipment</div>
  <div class="circle-arrow" style="left:262px;top:1642px"><svg width="12" height="12" viewBox="0 0 12 12"><path d="M4 2l4 4-4 4" stroke="#fff" stroke-width="1.6" fill="none"/></svg></div>
  <div class="circle-arrow" style="left:899px;top:1642px"><svg width="12" height="12" viewBox="0 0 12 12"><path d="M4 2l4 4-4 4" stroke="#fff" stroke-width="1.6" fill="none"/></svg></div>
  <a class="btn btn-solid more-btn">More</a>
  <h2 class="section-title services-title">Our Services</h2>
  <p class="services-text">Providing you with honest straightforward service is our number one goal. We manufacture finished metal and plastic goods to tight tolerances using technologically advanced equipment. Our spotlight is multi-featured products manufactured on 7 plus axis world-class screw machines. Our ideal sizes, not our limits, are from .02 to 1.25 inches diameter by .250 to 5.00 inches in length. Cross holes, wrench flats or something new to us all, completed in one operation. Whether you need to make one or a million our screw machine department is capable of fulfilling your need.</p>
  <a class="btn btn-solid explore-btn">Explore More</a>
</section>

<section class="industries">
  <h2 class="section-title" style="top:120px">Industries We Served</h2>
  <svg class="carousel-arrow" style="left:62px" width="14" height="24" viewBox="0 0 14 24"><path d="M12 2L3 12l9 10" stroke="#9aa0aa" stroke-width="2" fill="none"/></svg>
  <svg class="carousel-arrow" style="left:1116px" width="14" height="24" viewBox="0 0 14 24"><path d="M2 2l9 10-9 10" stroke="#9aa0aa" stroke-width="2" fill="none"/></svg>
  <div class="industry" style="left:150px">
    <svg width="40" height="40" viewBox="0 0 40 40" fill="none" stroke="#2a3f99" stroke-width="2"><path d="M6 26l28-14M18 20l-6-10h4l10 8M22 22l2 10h-4l-6-8M8 24l-2-6 4 3"/></svg>Aerospace</div>
  <div class="industry" style="left:340px">
    <svg width="40" height="40" viewBox="0 0 40 40" fill="none" stroke="#2a3f99" stroke-width="2"><circle cx="20" cy="20" r="15"/><circle cx="20" cy="20" r="4"/><path d="M6 18h10M24 18h10M20 24v11"/></svg>Automotive</div>
  <div class="industry" style="left:530px">
    <svg width="40" height="40" viewBox="0 0 40 40" fill="none" stroke="#2a3f99" stroke-width="2"><rect x="5" y="7" width="30" height="20" rx="2"/><path d="M16 27v6M24 27v6M12 33h16"/></svg>Computer</div>
  <div class="industry" style="left:720px">
    <svg width="40" height="40" viewBox="0 0 40 40" fill="none" stroke="#2a3f99" stroke-width="2"><path d="M12 6c4 0 5 2 8 2s4-2 8-2c5 0 6 6 5 11-1 4-3 6-4 12-1 5-4 5-5 0l-1-6c-1-3-5-3-6 0l-1 6c-1 5-4 5-5 0-1-6-3-8-4-12-1-5 0-11 5-11z"/></svg>Dental</div>
  <div class="industry" style="left:910px">
    <svg width="40" height="40" viewBox="0 0 40 40" fill="none" stroke="#2a3f99" stroke-width="2"><circle cx="20" cy="20" r="15"/><path d="M16 12v8M24 12v8M13 20h14v3a7 7 0 0 1-14 0zM20 30v5"/></svg>Electronics</div>
</section>

<section class="testimonials">
  <svg width="1200" height="500" viewBox="0 0 1200 500" style="position:absolute;left:0;top:0"><path d="M0 0H1200V470C1000 420 820 360 620 420C420 480 200 470 0 380Z" fill="#1d3f8c"/></svg>
  <h2 class="section-title">Testimonials</h2>
  <p class="quote">"I love working with engineers. Finding ways to make their parts less expensive is a puzzle I never get tired of solving."</p>
  <div class="avatar" role="img" aria-label="Portrait photograph of the company founder"></div>
  <div class="person">Daniel Verhoef<span>Founder</span></div>
</section>

<section class="quote-form">
  <h2 class="section-title">Get Free Quotes</h2>
  <div class="field" style="left:199px;top:3387px;width:390px">Enter your Name</div>
  <div class="field" style="left:199px;top:3449px;width:390px">Email</div>
  <div class="field" style="left:199px;top:3513px;width:390px">Phone</div>
  <div class="field" style="left:199px;top:3577px;width:390px">Company Name</div>
  <div class="field" style="left:611px;top:3387px;width:387px">Equipment Regarding</div>
  <div class="field area" style="left:611px;top:3449px;width:387px;height:168px">Type your Message...</div>
  <a class="btn btn-solid submit-btn">Submit</a>
</section>

<footer class="site-footer">
  <svg class="footer-bg" width="1200" height="404" viewBox="0 0 1200 404"><path d="M0 60C200 0 420 40 640 80C860 120 1040 60 1200 20V404H0Z" fill="#363b45"/></svg>
  <div class="wordmark"><span class="dot"></span>Corvel Ridge</div>
  <div class="footer-col" style="left:199px">
    <h4>Contact Us</h4>
    <div class="big">Call Us: 555-214-7731</div>
    <div>E: info@corvelridgemachining.example</div>
    <div style="margin-top:14px;color:#fff">Corvel Ridge Manufacturing Inc.</div>
    <div>4120 Halvern Way, Marrowfield,<br>CA 90000</div>
  </div>
  <div class="footer-col" style="left:519px">
    <h4>Equipment</h4>
    <div>Machining Equipment</div><div>Qa Equipment</div><div>Support Equipment</div>
  </div>
  <div class="footer-col" style="left:760px">
    <h4>Quick Links</h4>
    <div class="active">About Us</div><div>Services</div><div>Equipment</div><div>Quality</div><div>Contact Us</div>
  </div>
  <span class="social" style="top:3936px"></span>
  <span class="social" style="top:3978px"></span>
  <span class="social" style="top:4020px"></span>
  <div class="footer-bar">© 2019 Corvel Ridge Manufacturing Inc. All Right Reserved</div>
</footer>

</body>
</html>
```